Redesign start page for existing online shop

We are selling building material (chimneys and flue pipes) as well as fireplaces (stoves). For this online shop we need a new start page. The domain is brunnfeld-bauwaren.de. Here you can see the current design. We want a smoother design with just one banner in the middle instead of the three in the first row. The look has to be more professional and trustworthy. You can therefore play with the colors. We want to try some different orange instead of our yellow / orange color. A few more things: - The phone number has to be bigger and more highlighted - So the 5 advantages at the top should be shown in a different way - New design for the products below - New footer

Target Market(s)

Germany and other countries in Europe.

Industry/Entity Type

Home Builder

Number of Pages Required

1 page

Other font styles liked:
• Please se the font on our current site.

Colors
f78f20
f68d4c

Requirements
Must have
• - Clear design - Trustworthy look - All elements Which are now shown shoulderstand be still there after redesigning -
Nice to have
• - See the Following sites to have a clou about our wishes: kalvesto.de flinkrabe.de

```html
<!DOCTYPE html>
<html lang="en">
<head>
<meta charset="utf-8">
<title>Brunnfeld Bauwaren – Start</title>
<link href="https://fonts.googleapis.com/css2?family=Open+Sans:wght@400;600;700&family=Oswald:wght@500;700&display=swap" rel="stylesheet">
<style>
:root{
  --orange:#f78f20;
  --orange-soft:#f68d4c;
  --dark:#2a2e33;
  --darker:#1f2226;
  --grey:#f2f2f2;
  --line:#e1e1e1;
  --text:#333;
  --muted:#777;
  --white:#fff;
}
*{box-sizing:border-box;margin:0;padding:0}
html,body{width:1200px;height:3040px;overflow:hidden}
body{font-family:"Open Sans",Arial,sans-serif;color:var(--text);background:var(--white);font-size:13px}
.wrap{width:1040px;margin:0 auto}
a{color:inherit;text-decoration:none}

.topbar{height:40px;background:var(--darker);color:#bbb;font-size:11px}
.topbar .wrap{display:flex;justify-content:space-between;align-items:center;height:40px}
.topbar span{margin-right:18px}

.header{height:100px}
.header .wrap{display:flex;align-items:center;height:100px;gap:30px}
.brand{display:flex;align-items:center;gap:10px;font-weight:700;font-size:22px;color:var(--dark)}
.brand i{width:30px;height:30px;background:var(--orange);display:block}
.search{flex:1;height:36px;border:1px solid var(--line);border-radius:3px;display:flex;align-items:center;padding:0 12px;color:#aaa;font-size:12px}
.seal{width:44px;height:44px;border-radius:50%;background:#ddd}
.hotline{display:flex;align-items:center;gap:10px}
.hotline .ic{width:40px;height:40px;border-radius:50%;background:var(--orange);display:flex;align-items:center;justify-content:center}
.hotline b{font-size:26px;color:var(--orange);display:block;line-height:1}
.hotline small{font-size:10px;color:var(--muted)}

.nav{height:30px;background:var(--dark);color:#fff;font-size:11px;font-weight:600}
.nav .wrap{display:flex;align-items:center;height:30px;gap:28px}
.nav .advisor{margin-left:auto;color:var(--orange)}

.hero{height:300px;position:relative;background:linear-gradient(90deg,#8aa3b6 0%,#a9b8c2 50%,#2f80c1 70%,#2a6fa8 100%)}
.hero .wrap{position:relative;height:300px}
.hero-copy{position:absolute;right:0;top:70px;text-align:right;color:#fff;font-family:Oswald,Arial,sans-serif}
.hero-copy h1{font-size:54px;line-height:1.05;font-weight:700}
.hero-copy h1 span{color:var(--orange)}
.btn{display:inline-block;background:var(--orange);color:#fff;font-weight:700;font-size:11px;padding:10px 22px;border-radius:2px;text-transform:uppercase}
.hero-copy .btn{margin-top:22px;font-family:"Open Sans",Arial,sans-serif}

.brands{height:70px;border-bottom:1px solid var(--line)}
.brands .wrap{display:flex;align-items:center;justify-content:space-between;height:70px;color:#999;font-size:20px;font-weight:600}
.brands .arrow{color:#ccc}

.usp{margin-top:60px;height:40px;background:var(--orange);color:#fff;font-weight:700;font-size:12px}
.usp .wrap{display:flex;align-items:center;height:40px;gap:40px}
.usp .more{margin-left:auto;background:#fff;color:var(--orange);padding:6px 16px;font-size:15px}
.usp span::before{content:"✓ "}

.features{height:160px;background:var(--dark);color:#ddd}
.features .wrap{display:flex;justify-content:space-between;height:160px;align-items:center;padding:0 40px}
.feature{width:150px;text-align:center;font-size:10px;font-weight:600;text-transform:uppercase;line-height:1.4}
.feature svg{display:block;margin:0 auto 12px}

.products{height:720px;padding-top:26px}
.grid{display:grid;grid-template-columns:repeat(4,1fr);gap:24px}
.card{height:320px;border:1px solid var(--line);padding:14px;display:flex;flex-direction:column}
.card .pic{height:150px;background:linear-gradient(160deg,#eceff1,#c5ccd2)}
.card h3{font-size:14px;text-align:center;margin:14px 0 6px}
.card p{font-size:10px;color:var(--muted);text-align:center;line-height:1.4;flex:1}
.card .buy{display:flex;justify-content:space-between;align-items:center;background:var(--orange);color:#fff;font-size:11px;font-weight:700;padding:7px 10px}
.card .buy em{font-style:normal;background:#fff;color:var(--orange);padding:2px 8px;font-size:10px}

.consult{height:350px;display:flex}
.consult .left{width:50%;background:var(--orange);color:#fff;padding:44px 40px 0 80px}
.consult .right{width:50%;background:var(--dark);color:#ddd;padding:50px 80px 0 50px;text-align:center}
.consult h2{font-size:22px;margin-bottom:26px}
.steps{display:flex;gap:30px;margin-bottom:22px}
.step{font-size:10px;font-weight:600;text-align:center;width:110px}
.step svg{display:block;margin:0 auto 8px}
.consult .left p{font-size:11px;line-height:1.5;max-width:440px;margin-bottom:20px}
.btn-white{display:inline-block;background:#fff;color:var(--orange);font-weight:700;font-size:10px;padding:9px 18px}
.consult .right h2{color:#fff;font-size:18px;margin:14px 0 8px}
.consult .right p{font-size:11px;line-height:1.5;margin-bottom:22px}
.price-row{display:flex;justify-content:center;gap:12px}
.price-row span{background:#fff;color:var(--dark);font-size:10px;font-weight:700;padding:9px 14px}

.seo{height:690px;padding-top:36px}
.seo h2{font-size:18px;color:var(--dark);margin-bottom:22px}
.seo .body{display:flex;gap:34px}
.seo .pic{width:330px;height:260px;flex:none;background:linear-gradient(180deg,#9cc2e3 0%,#d9e4ea 55%,#b9b0a0 100%)}
.seo .text p{font-size:11px;line-height:1.7;color:#555;margin-bottom:12px}
.seo .text h4{font-size:12px;margin:6px 0 10px;color:var(--dark)}

.safe{height:100px;border-top:1px solid var(--line)}
.safe .wrap{display:flex;align-items:center;height:100px;gap:26px}
.safe h3{font-size:22px;color:var(--dark);width:150px;line-height:1.1}
.safe .badge{width:52px;height:52px;border-radius:50%;background:#ddd;flex:none}
.safe p{font-size:10px;color:var(--muted);line-height:1.5;width:330px}

.payment{height:100px;padding-top:15px}
.payment .band{height:70px;background:var(--orange)}
.payment .wrap{display:flex;align-items:center;height:70px;gap:16px}
.payment h3{color:#fff;font-size:18px;width:220px}
.payment span{background:#fff;color:var(--dark);font-size:11px;font-weight:700;width:92px;height:36px;display:flex;align-items:center;justify-content:center;border-radius:2px}

.footer{height:280px;background:var(--dark);color:#aaa;font-size:11px}
.footer .cols{display:flex;gap:40px;padding-top:30px;height:230px}
.footer h4{color:#fff;font-size:13px;margin-bottom:12px}
.footer ul{list-style:none;line-height:2}
.footer .col{flex:1}
.footer .phone{color:var(--orange);font-size:22px;font-weight:700;margin:4px 0 10px}
.socials{display:flex;gap:8px;margin-top:10px}
.socials i{width:24px;height:24px;border-radius:50%;background:#444b52;display:block}
.footer .bottom{height:50px;background:var(--darker);display:flex;align-items:center;justify-content:center;font-size:10px;color:#888}
</style>
</head>
<body>

<div class="topbar"><div class="wrap">
  <div><span>☎ 0800/482 771 0</span><span>✉ info@brunnfeld-bauwaren.de</span></div>
  <div><span>My account</span><span>Contact</span><span>Blog</span></div>
</div></div>

<header class="header"><div class="wrap">
  <div class="brand"><i></i>Brunnfeld Bauwaren</div>
  <div class="search">Search for products …</div>
  <div class="seal" aria-hidden="true"></div>
  <div class="hotline">
    <div class="ic"><svg width="18" height="18" viewBox="0 0 24 24"><path fill="#fff" d="M6.6 10.8a15.1 15.1 0 006.6 6.6l2.2-2.2a1 1 0 011-.25 11.4 11.4 0 003.6.57 1 1 0 011 1V20a1 1 0 01-1 1A17 17 0 013 4a1 1 0 011-1h3.5a1 1 0 011 1c0 1.25.2 2.45.57 3.57a1 1 0 01-.25 1z"/></svg></div>
    <div><b>0800/482 771 0</b><small>Mon–Fri 8:00–17:00 free advice</small></div>
  </div>
</div></header>

<nav class="nav"><div class="wrap">
  <span>ONLINE SHOP ▾</span><span>SERVICE ▾</span><span>CHIMNEYS ▾</span><span>FOR DEALERS ▾</span><span>INSTALLATION ▾</span>
  <span class="advisor">● Product Advisor</span><span>My Account</span><span>Cart 0</span>
</div></nav>

<section class="hero">
  <div class="wrap">
    <div class="hero-copy">
      <h1>IN 5 MINUTES<br><span>TO HEATING</span><br>SUPPLY</h1>
      <a class="btn" href="#">Offer advice</a>
    </div>
  </div>
  <div role="img" aria-label="Installer in a yellow hard hat holding a hand tool, with a tool belt" style="position:absolute;left:0;top:0;width:560px;height:300px;background:linear-gradient(120deg,#c9cdd0,#9fb1c0)"></div>
</section>

<section class="brands"><div class="wrap">
  <span class="arrow">‹</span><span>Calvora</span><span>Calvora</span><span>Tarnex</span><span>Calvora</span><span>Tarnex</span><span>Calvora</span><span class="arrow">›</span>
</div></section>

<section class="usp"><div class="wrap">
  <span>TOP CONSULTING</span><span>BEST PRICE GUARANTEE</span><span>FAST DELIVERY</span>
  <a class="more" href="#">DISCOVER NOW ›</a>
</div></section>

<section class="features"><div class="wrap">
  <div class="feature"><svg width="40" height="40" viewBox="0 0 40 40" fill="none" stroke="#f78f20" stroke-width="2"><circle cx="20" cy="20" r="16"/><path d="M13 20l5 5 9-10"/></svg>Original<br>brand quality</div>
  <div class="feature"><svg width="40" height="40" viewBox="0 0 40 40" fill="none" stroke="#f78f20" stroke-width="2"><path d="M20 4l14 6v10c0 9-6 14-14 16C12 34 6 29 6 20V10z"/></svg>30 year<br>warranty</div>
  <div class="feature"><svg width="40" height="40" viewBox="0 0 40 40" fill="none" stroke="#f78f20" stroke-width="2"><rect x="3" y="12" width="22" height="14"/><path d="M25 16h7l5 5v5H25"/><circle cx="11" cy="29" r="3"/><circle cx="31" cy="29" r="3"/></svg>Fast<br>delivery</div>
  <div class="feature"><svg width="40" height="40" viewBox="0 0 40 40" fill="none" stroke="#f78f20" stroke-width="2"><path d="M6 8h28v18H18l-8 6v-6H6z"/></svg>Free<br>consultation</div>
  <div class="feature"><svg width="40" height="40" viewBox="0 0 40 40" fill="none" stroke="#f78f20" stroke-width="2"><path d="M26 6a8 8 0 00-9 10L6 27l7 7 11-11a8 8 0 0010-9l-5 5-5-1-1-5z"/></svg>Nationwide<br>installation service</div>
</div></section>

<section class="products"><div class="wrap grid">
  <article class="card"><div class="pic" role="img" aria-label="Stainless steel chimney extension"></div><h3>Chimney Extension</h3><p>Fireplace extension configurable, professionally installed.</p><div class="buy">ab € 89,00 <em>ADD TO CART</em></div></article>
  <article class="card"><div class="pic" role="img" aria-label="Chimney cowl"></div><h3>Chimney Cowl</h3><p>Protects the flue against rain and downdraft.</p><div class="buy">ab € 59,00 <em>ADD TO CART</em></div></article>
  <article class="card"><div class="pic" role="img" aria-label="Wall bushing set"></div><h3>Wall bushing</h3><p>Wall penetrations for the safe run of exhaust pipes.</p><div class="buy">ab € 45,00 <em>ADD TO CART</em></div></article>
  <article class="card"><div class="pic" role="img" aria-label="Black stovepipe elbow"></div><h3>Stovepipe</h3><p>Under stovepipes in black or grey, premium quality.</p><div class="buy">ab € 29,00 <em>ADD TO CART</em></div></article>
  <article class="card"><div class="pic" role="img" aria-label="Lightweight construction chimney"></div><h3>Lightweight Construction Chimney</h3><p>Lightweight chimney systems for the perfect solution.</p><div class="buy">ab € 799,00 <em>ADD TO CART</em></div></article>
  <article class="card"><div class="pic" role="img" aria-label="Fireplace cleaning door"></div><h3>Fireplace Door</h3><p>Fireplace doors and flush doors made of stainless steel.</p><div class="buy">ab € 39,00 <em>ADD TO CART</em></div></article>
  <article class="card"><div class="pic" role="img" aria-label="Wood burning stove with fire"></div><h3>Stove</h3><p>Stoves with excellent price, modern design and flame.</p><div class="buy">ab € 649,00 <em>ADD TO CART</em></div></article>
  <article class="card"><div class="pic" role="img" aria-label="Chimney fan unit"></div><h3>Chimney Fans</h3><p>Chimney fans for the perfect draft of the chimney.</p><div class="buy">ab € 299,00 <em>ADD TO CART</em></div></article>
</div></section>

<section class="consult">
  <div class="left">
    <h2>Arrange An Appointment For Consultation</h2>
    <div class="steps">
      <div class="step"><svg width="30" height="30" viewBox="0 0 30 30" fill="none" stroke="#fff" stroke-width="2"><rect x="4" y="6" width="22" height="20"/><path d="M4 12h22M10 3v6M20 3v6"/></svg>Book the desired date</div>
      <div class="step"><svg width="30" height="30" viewBox="0 0 30 30" fill="none" stroke="#fff" stroke-width="2"><circle cx="15" cy="10" r="5"/><path d="M5 27c1-6 5-9 10-9s9 3 10 9"/></svg>Contact specialist</div>
      <div class="step"><svg width="30" height="30" viewBox="0 0 30 30" fill="none" stroke="#fff" stroke-width="2.5"><path d="M6 15l6 6 12-13"/></svg>Book expert advice</div>
    </div>
    <p>Here you have the chance to comfortably arrange your call. An expert by your side will then advise you on the right chimney products and flue components. Please fill out the form below and specify the desired date.</p>
    <a class="btn-white" href="#">BOOK NOW ADVICE ›</a>
  </div>
  <div class="right">
    <svg width="70" height="70" viewBox="0 0 70 70" fill="none" stroke="#fff" stroke-width="2"><circle cx="35" cy="35" r="33"/><path d="M42 20a9 9 0 00-10 11L20 43l7 7 12-12a9 9 0 0011-10l-6 6-6-1-1-6z"/></svg>
    <h2>MOUNTING SERVICE</h2>
    <p>Have your new chimney installed by professionals at an unbeatable fixed price.</p>
    <div class="price-row"><span>From € 399,00</span><a class="btn" href="#">Assembly now book</a></div>
  </div>
</section>

<section class="seo"><div class="wrap">
  <h2>Stainless steel chimneys, chimney extensions, stovepipes and chimney accessories - at brunnfeld-bauwaren.de buy</h2>
  <div class="body">
    <div class="pic" role="img" aria-label="Modern house with a stainless steel chimney on the facade"></div>
    <div class="text">
      <p>Can I use a stainless steel chimney for use on the exterior? The question you have probably never asked. For older products we offer a matter of course, but with a stainless steel chimney you do not limit the fireplace to an existing chimney. There are many options for a stove in every house and we will help you choose the right solution for your building.</p>
      <p>Stainless steel chimneys are installed quickly, need very little space and are extremely durable. At brunnfeld-bauwaren.de you find complete kits, single components and all accessories from renowned manufacturers. Our team checks every request personally so that your project fits local regulations and is approved by the chimney sweep.</p>
      <p>We deliver fast throughout Germany and Europe, offer fair prices and provide full technical support. Whether you plan a new installation, a renovation or just need spare parts, you will find the right product here.</p>
      <h4>Stove chimney, chimney kit and stainless steel chimney - all from one source.</h4>
      <p>Whether you have a double walled stainless steel chimney or a chimney extension, our advisors are ready to help you choose. Just call us or use the product advisor and get a tailored offer within one working day.</p>
    </div>
  </div>
</div></section>

<section class="safe"><div class="wrap">
  <h3>Shopping<br>Safely</h3>
  <div class="badge" aria-hidden="true"></div>
  <p>We offer consumer protection for every purchase. Our shop is regularly audited and all personal data is transferred encrypted and stored securely.</p>
  <div class="badge" aria-hidden="true"></div>
  <p>Our shop is certified for quality and service. Customers rate us with top marks for delivery, advice and reliability.</p>
</div></section>

<section class="payment"><div class="band"><div class="wrap">
  <h3>Payment Methods:</h3>
  <span>CardOne</span><span>Direct Debit</span><span>WalletPay</span><span>Invoice</span><span>Prepay</span><span>CardTwo</span><span>BankLink</span>
</div></div></section>

<footer class="footer">
  <div class="wrap cols">
    <div class="col"><h4>Quick Link</h4><ul><li>Frequently Asked</li><li>Conditions</li><li>Delivery</li><li>Conditions</li><li>Imprint</li></ul></div>
    <div class="col"><h4>&nbsp;</h4><ul><li>About Us</li><li>Privacy</li><li>Returns</li><li>Blog</li><li>Glossary</li></ul></div>
    <div class="col"><h4>Contact Us</h4><ul><li>Brunnfeld Bauwaren GmbH</li><li>Lindenweg 14</li><li>80000 Musterstadt</li><li>Germany</li><li>info@brunnfeld-bauwaren.de</li></ul></div>
    <div class="col"><h4>Free Consultation</h4><div class="phone">0800/482 771 0</div><div>Mon–Fri 8:00 – 17:00</div><div class="socials"><i></i><i></i><i></i><i></i><i></i></div></div>
  </div>
  <div class="bottom">© Brunnfeld Bauwaren · All prices incl. VAT plus shipping</div>
</footer>

</body>
</html>
```